new KVR one page flyer

We need a 1 page A4 size flyer (need it asap please) that describes on 1 page with art work and using photos the services we provide. I have included some examples of old previous flyers from our other (seperate divisions of the business) I have named a photo called (photo for top of design) however you do your design this photo needs to be the star of the page by either having it at the top or bottom of the page please and we usually like this photo to be in greyscale colour.
we do like greyscale designs but are open to see what you come up with as a whole page of grey white and black might not suit.

Needs to list the following

Services include:
Over size loads / Hot Shot Loads
Heavy Vehicle Recovery services
Potable Water Deliveries
Road Building / Maintenance
Earthworks
Sand & Metal Supply & Cartage
Road Train Tippers
Road Train Tankers
Road Train Flat Tops
Drop Deck Trailers
Mine site accredited equipment & Operators.

We offer a large rage of services not listed so call us today for a personalised quote to suit your needs.

To go on the bottom of the page our contact details are

KVR Pty Ltd
Depot: Lot 514, Banksia Flats Track Emu Ridge
Mobile: 047 216 9381
email: darren@kestrelvaleroadworks.com.au

Target Market(s)

new clients

Colors

Designer to choose colors to be used in the design.

Requirements
Must have
• our services listed
Nice to have
• stand out designs

```html
<!DOCTYPE html>
<html lang="en">
<head>
<meta charset="utf-8">
<title>KVR Flyer</title>
<link href="https://fonts.googleapis.com/css2?family=Jost:wght@400;500;600&display=swap" rel="stylesheet">
<style>
  :root{
    --page-bg:#e4e4e6;
    --paper:#ffffff;
    --ink:#1b1a2a;
    --ink-soft:#555559;
    --sky-top:#aeb3e2;
    --sky-mid:#c9cbe9;
    --dust:#d9d0c2;
    --band-dark:#1d1c2c;
    --band-mid:#3a3440;
    --footer-left:#4a4a52;
    --footer-right:#1c1b2e;
    --white:#ffffff;
    --rule:#d8d8e0;
  }
  *{box-sizing:border-box;margin:0;padding:0}
  html,body{width:1200px;height:1200px;overflow:hidden}
  body{background:var(--page-bg);font-family:'Jost',sans-serif;position:relative}
  .flyer{position:absolute;left:207px;top:44px;width:786px;height:1112px;background:var(--paper);overflow:hidden}
  .hero-photo{position:absolute;left:0;top:0;width:786px;height:560px;
    background:linear-gradient(180deg,var(--sky-top) 0%,var(--sky-mid) 40%,var(--dust) 75%,var(--paper) 100%)}
  .hero-wedge{position:absolute;left:0;top:0}
  .brand{position:absolute;left:48px;top:40px;font-size:92px;font-weight:600;color:var(--ink);letter-spacing:2px;line-height:1}
  .title{position:absolute;left:0;width:786px;text-align:center;line-height:1;text-transform:uppercase}
  .title-top{top:404px;font-size:66px;font-weight:400;color:var(--ink-soft)}
  .title-main{top:486px;font-size:70px;font-weight:500;color:var(--ink)}
  .services-heading{position:absolute;top:592px;left:0;width:786px;text-align:center;font-size:50px;font-weight:400;color:#2c2b38}
  .services-band{position:absolute;left:0;top:666px;width:786px;height:268px;
    background:linear-gradient(100deg,var(--band-mid) 0%,var(--band-dark) 45%,#25222e 70%,var(--band-dark) 100%)}
  .services-divider{position:absolute;left:401px;top:686px;width:1px;height:230px;background:var(--rule);opacity:.7}
  .service-list{position:absolute;list-style:none;color:var(--white);font-size:20px;font-weight:400}
  .service-list li{position:absolute;white-space:nowrap;display:flex;align-items:center;line-height:1}
  .service-list .tick{width:11px;height:11px;margin-right:13px;flex:none}
  .list-left{left:52px;top:0}
  .list-right{left:437px;top:0}
  .list-right li.wrap{align-items:flex-start;line-height:35px;white-space:normal;width:300px}
  .list-right li.wrap .tick{margin-top:12px}
  .cta{position:absolute;top:950px;left:0;width:786px;text-align:center;font-size:17px;line-height:26px;color:var(--ink);text-transform:uppercase}
  .contact-bar{position:absolute;left:0;top:1010px;width:786px;height:102px;
    background:linear-gradient(90deg,var(--footer-left) 0%,#2c2b38 55%,var(--footer-right) 100%);color:var(--white)}
  .contact-phone{position:absolute;left:32px;top:30px;display:flex;align-items:center}
  .contact-phone span{font-size:37px;font-weight:400;margin-left:18px;letter-spacing:1px}
  .contact-rule{position:absolute;top:22px;width:1px;height:66px;background:var(--white);opacity:.8}
  .contact-address{position:absolute;left:342px;width:180px;top:14px;text-align:center;font-size:13px;line-height:16px}
  .contact-address svg{display:block;margin:0 auto 10px}
  .contact-email{position:absolute;left:523px;width:263px;top:18px;text-align:center;font-size:12.5px}
  .contact-email svg{display:block;margin:0 auto 20px}
  .contact-email b{font-weight:600}
</style>
</head>
<body>
  <main class="flyer">
    <div class="hero-photo" role="img" aria-label="Photo of a white road train water tanker parked in a dusty depot yard under a blue sky"></div>
    <svg class="hero-wedge" width="786" height="560" viewBox="0 0 786 560">
      <polygon points="0,0 330,0 0,244" fill="#ffffff" opacity="0.35"/>
    </svg>
    <div class="brand">KVR</div>

    <h1 class="title title-top">Kestrel Vale</h1>
    <h1 class="title title-main">Road Services</h1>

    <h2 class="services-heading">Services include:</h2>

    <div class="services-band" role="img" aria-label="Darkened photo of road trains lined up at the depot at dusk"></div>
    <div class="services-divider"></div>

    <ul class="service-list list-left">
      <li style="top:694px"><svg class="tick" viewBox="0 0 12 12"><circle cx="6" cy="6" r="5" fill="none" stroke="#fff" stroke-width="1.2"/><path d="M3.5 6.2l1.8 1.7 3.3-3.6" fill="none" stroke="#fff" stroke-width="1.2"/></svg>Over size loads / Hot Shot Loads</li>
      <li style="top:732px"><svg class="tick" viewBox="0 0 12 12"><circle cx="6" cy="6" r="5" fill="none" stroke="#fff" stroke-width="1.2"/><path d="M3.5 6.2l1.8 1.7 3.3-3.6" fill="none" stroke="#fff" stroke-width="1.2"/></svg>Heavy Vehicle Recovery services</li>
      <li style="top:774px"><svg class="tick" viewBox="0 0 12 12"><circle cx="6" cy="6" r="5" fill="none" stroke="#fff" stroke-width="1.2"/><path d="M3.5 6.2l1.8 1.7 3.3-3.6" fill="none" stroke="#fff" stroke-width="1.2"/></svg>Potable Water Deliveries</li>
      <li style="top:812px"><svg class="tick" viewBox="0 0 12 12"><circle cx="6" cy="6" r="5" fill="none" stroke="#fff" stroke-width="1.2"/><path d="M3.5 6.2l1.8 1.7 3.3-3.6" fill="none" stroke="#fff" stroke-width="1.2"/></svg>Road Building / Maintenance</li>
      <li style="top:852px"><svg class="tick" viewBox="0 0 12 12"><circle cx="6" cy="6" r="5" fill="none" stroke="#fff" stroke-width="1.2"/><path d="M3.5 6.2l1.8 1.7 3.3-3.6" fill="none" stroke="#fff" stroke-width="1.2"/></svg>Earthworks</li>
      <li style="top:890px"><svg class="tick" viewBox="0 0 12 12"><circle cx="6" cy="6" r="5" fill="none" stroke="#fff" stroke-width="1.2"/><path d="M3.5 6.2l1.8 1.7 3.3-3.6" fill="none" stroke="#fff" stroke-width="1.2"/></svg>Drop Deck Trailers</li>
    </ul>

    <ul class="service-list list-right">
      <li style="top:692px"><svg class="tick" viewBox="0 0 12 12"><circle cx="6" cy="6" r="5" fill="none" stroke="#fff" stroke-width="1.2"/><path d="M3.5 6.2l1.8 1.7 3.3-3.6" fill="none" stroke="#fff" stroke-width="1.2"/></svg>Sand &amp; Metal Supply &amp; Cartage</li>
      <li style="top:734px"><svg class="tick" viewBox="0 0 12 12"><circle cx="6" cy="6" r="5" fill="none" stroke="#fff" stroke-width="1.2"/><path d="M3.5 6.2l1.8 1.7 3.3-3.6" fill="none" stroke="#fff" stroke-width="1.2"/></svg>Road Train Tippers</li>
      <li style="top:774px"><svg class="tick" viewBox="0 0 12 12"><circle cx="6" cy="6" r="5" fill="none" stroke="#fff" stroke-width="1.2"/><path d="M3.5 6.2l1.8 1.7 3.3-3.6" fill="none" stroke="#fff" stroke-width="1.2"/></svg>Road Train Tankers</li>
      <li style="top:812px"><svg class="tick" viewBox="0 0 12 12"><circle cx="6" cy="6" r="5" fill="none" stroke="#fff" stroke-width="1.2"/><path d="M3.5 6.2l1.8 1.7 3.3-3.6" fill="none" stroke="#fff" stroke-width="1.2"/></svg>Road Train Flat Tops</li>
      <li class="wrap" style="top:838px"><svg class="tick" viewBox="0 0 12 12"><circle cx="6" cy="6" r="5" fill="none" stroke="#fff" stroke-width="1.2"/><path d="M3.5 6.2l1.8 1.7 3.3-3.6" fill="none" stroke="#fff" stroke-width="1.2"/></svg><span>Mine site accredited<br>equipment &amp; Operators.</span></li>
    </ul>

    <p class="cta">We offer a large rage of services not listed so call us today for<br>a personalised quote to suit your needs.</p>

    <footer class="contact-bar">
      <div class="contact-phone">
        <svg width="40" height="40" viewBox="0 0 40 40">
          <circle cx="20" cy="20" r="17.5" fill="none" stroke="#fff" stroke-width="3"/>
          <path d="M13 12c1-1 2.5-1 3.3 0l2 2.6c.6.8.5 1.8-.2 2.4l-1.2 1c.9 2 2.5 3.7 4.6 4.7l1-1.2c.6-.7 1.7-.8 2.4-.2l2.6 2c1 .8 1 2.3 0 3.3l-1.3 1.2c-1.3 1.2-3.3 1.4-4.9.5-4.3-2.3-7.6-5.6-9.7-9.9-.8-1.6-.5-3.5.7-4.8z" fill="#fff"/>
        </svg>
        <span>047 216 9381</span>
      </div>
      <div class="contact-rule" style="left:341px"></div>
      <div class="contact-address">
        <svg width="20" height="26" viewBox="0 0 20 26"><path d="M10 1C5 1 1.5 4.8 1.5 9.5 1.5 16 10 25 10 25s8.5-9 8.5-15.5C18.5 4.8 15 1 10 1z" fill="#fff"/><circle cx="10" cy="9.5" r="3.3" fill="#3a3944"/></svg>
        Lot 514, Banksia Flats Track<br>Emu Ridge
      </div>
      <div class="contact-rule" style="left:522px"></div>
      <div class="contact-email">
        <svg width="28" height="18" viewBox="0 0 28 18"><rect x="1" y="1" width="26" height="16" fill="#fff"/><path d="M1 1l13 10L27 1" fill="none" stroke="#2c2b38" stroke-width="1.6"/></svg>
        darren@<b>kestrelvaleroadworks</b>.com.au
      </div>
    </footer>
  </main>
</body>
</html>
```